Startup company business card (Media & Advertising)

we need a business card design for a company that is a startup in the media and aggregation industry. Card needs to look funky and of a new breed/modern and upmarket.

Target Market(s)

advertisers/ brand agencies & media publishers

Industry/Entity Type

Advertising

Contact Information for Business Card

Please ensure the front face signifies our brand (plumvexo.com) and back has details for the contact. Standard contact such as phone , address, email , website etc.

Font styles to use
Other font styles liked:
• use styleguide and logo font and color

Colors

Designer to choose colors to be used in the design.

Requirements
Must have
• We are disrupting the media and agency industry so subtlety would be good to use imagery to signify this
Nice to have
• Please use logo colors for branding
Should not have
• be as creative and provide few options. Pick a brand color from logo and styleguide

```html
<!DOCTYPE html>
<html lang="en">
<head>
<meta charset="utf-8">
<title>Plumvexo Business Card</title>
<link rel="stylesheet" href="https://fonts.googleapis.com/css2?family=Montserrat:wght@400;500;700;800&display=swap">
<style>
  :root {
    --backdrop: #8d9094;
    --card: #ffffff;
    --brand-red: #ea3a42;
    --name-red: #d3283a;
    --ink: #111111;
    --text-grey: #4a4a4a;
    --edge-blue: #b9dcef;
  }
  * { box-sizing: border-box; margin: 0; padding: 0; }
  html, body { width: 1200px; height: 913px; overflow: hidden; }
  body {
    background: var(--backdrop);
    font-family: "Montserrat", Arial, sans-serif;
    position: relative;
  }
  .card {
    position: absolute;
    width: 580px;
    height: 330px;
    background: var(--card);
    box-shadow: 0 6px 0 var(--edge-blue), 0 14px 24px rgba(0,0,0,.25);
  }
  .card--contact { left: 50px; top: 70px; }
  .card--brand {
    left: 570px; top: 500px;
    box-shadow: 0 8px 0 var(--brand-red), 0 16px 24px rgba(0,0,0,.25);
  }

  /* contact face */
  .hero-mark {
    position: absolute;
    right: 120px; top: 26px;
    width: 170px; height: 170px;
    border-radius: 50%;
    background: linear-gradient(135deg, #f0484e, #c02540);
  }
  .contact__brand {
    position: absolute;
    right: 36px; bottom: 96px;
    display: flex; align-items: center; gap: 14px;
  }
  .brand-dot {
    width: 40px; height: 40px; border-radius: 50%;
    background: var(--brand-red);
  }
  .brand-name {
    font-weight: 800;
    color: var(--ink);
    letter-spacing: -0.5px;
  }
  .contact__brand .brand-name { font-size: 40px; }

  .person { position: absolute; left: 40px; top: 140px; }
  .person__name {
    color: var(--name-red);
    font-size: 22px; font-weight: 500; letter-spacing: .5px;
  }
  .person__role { color: var(--text-grey); font-size: 14px; margin-top: 2px; }
  .address {
    position: absolute; left: 40px; top: 208px;
    color: var(--text-grey); font-size: 14px; line-height: 1.35;
  }
  .contact-list {
    position: absolute; left: 40px; top: 250px;
    list-style: none; color: var(--text-grey); font-size: 14px;
  }
  .contact-list li { display: flex; align-items: center; gap: 10px; height: 19px; }
  .contact-list svg { width: 13px; height: 13px; fill: var(--brand-red); flex: none; }

  /* brand face */
  .brand-block {
    position: absolute; left: 70px; top: 105px;
    display: flex; align-items: center; gap: 26px;
  }
  .brand-block .brand-dot { width: 100px; height: 100px; }
  .brand-block .brand-name { font-size: 64px; line-height: 1; }
  .brand-url {
    margin-top: 8px;
    font-size: 14px; font-weight: 500; letter-spacing: 8px;
    color: var(--ink);
  }
</style>
</head>
<body>

<section class="card card--contact">
  <div class="hero-mark" role="img" aria-label="Large decorative brand mark area"></div>
  <div class="contact__brand">
    <span class="brand-dot"></span>
    <span class="brand-name">Plumvexo</span>
  </div>

  <div class="person">
    <p class="person__name">LENA OKAFOR</p>
    <p class="person__role">Director</p>
  </div>
  <p class="address">48 Corvel Avenue<br>204 Tavira, Portugal</p>

  <ul class="contact-list">
    <li>
      <svg viewBox="0 0 24 24"><path d="M6.6 10.8a15.1 15.1 0 0 0 6.6 6.6l2.2-2.2c.3-.3.7-.4 1-.2 1.1.4 2.3.6 3.6.6.6 0 1 .4 1 1V20c0 .6-.4 1-1 1A17 17 0 0 1 3 4c0-.6.4-1 1-1h3.5c.6 0 1 .4 1 1 0 1.3.2 2.5.6 3.6.1.3 0 .7-.2 1z"/></svg>
      1234567890
    </li>
    <li>
      <svg viewBox="0 0 24 24"><path d="M7 1h10a2 2 0 0 1 2 2v18a2 2 0 0 1-2 2H7a2 2 0 0 1-2-2V3a2 2 0 0 1 2-2zm0 3v14h10V4zm5 15.5a1 1 0 1 0 0 2 1 1 0 0 0 0-2z"/></svg>
      1234567890
    </li>
    <li>
      <svg viewBox="0 0 24 24"><path d="M2 5h20v14H2zm2 2v.5l8 5 8-5V7l-8 5z"/></svg>
      info@plumvexo.com
    </li>
    <li>
      <svg viewBox="0 0 24 24"><path d="M12 2a10 10 0 1 0 0 20 10 10 0 0 0 0-20zm6.9 6h-3a15 15 0 0 0-1.3-3.9A8 8 0 0 1 18.9 8zM12 4c.8 1.2 1.5 2.5 1.9 4h-3.8c.4-1.5 1.1-2.8 1.9-4zM4.3 14a8 8 0 0 1 0-4h3.4a16 16 0 0 0 0 4zm.8 2h3a15 15 0 0 0 1.3 3.9A8 8 0 0 1 5.1 16zm3-8h-3a8 8 0 0 1 4.3-3.9C8.8 5.3 8.4 6.6 8.1 8zM12 20c-.8-1.2-1.5-2.5-1.9-4h3.8c-.4 1.5-1.1 2.8-1.9 4zm2.3-6H9.7a14 14 0 0 1 0-4h4.6a14 14 0 0 1 0 4zm.3 5.9c.6-1.2 1-2.5 1.3-3.9h3a8 8 0 0 1-4.3 3.9zm1.7-5.9a16 16 0 0 0 0-4h3.4a8 8 0 0 1 0 4z"/></svg>
      www.plumvexo.com
    </li>
  </ul>
</section>

<section class="card card--brand">
  <div class="brand-block">
    <span class="brand-dot"></span>
    <div>
      <p class="brand-name">Plumvexo</p>
      <p class="brand-url">www.plumvexo.com</p>
    </div>
  </div>
</section>

</body>
</html>
```